Brochure design for small healthcare company

We need a 6 page tri-fold brochure. Finished, folded size is 5" x 7".

Attached to this brief: Brevicor logo (product), Tovandra logo (company) and MOCK up or layout - with all text and graphics in place. No design has been attempted on the layout.

This brochure will be given to patients to help them to understand their allergies.
They make a product that will allow a consumer to test for allergies in their own home. The product is called "Brevicor".

The brochure will need some graphic illustration - graphs and charts to explain allergies. Samples provided. Layout and copy provided. The graphs and images used in the sample mock up are for placement only. They are not to be taken literally. Just that the info is correct and something "Like" this is needed.

If photos are used they must be of people enjoying life - allergy free. No sick photos or clinical type (doctor) photos.
Updates

Yesterday - we posted a job for a brochure design. We thought we included a mock up / layout of the tri-fold brochure. Instead it was a photo. Sorry for the confusion. We have corrected the error and reposted the mock up and layout to the job. Please note that the graphs and charts used in the mock up / layout - are for information only. Your designs do NOT have to look like what is furnished. But all INFO in the supplied mock up text and text in the graphics/charts is correct. Thank you. Glen

Industry/Entity Type

Healthcare

```html
<!DOCTYPE html>
<html lang="en">
<head>
<meta charset="utf-8">
<title>Brevicor – Allergy Brochure Inside Spread</title>
<link rel="stylesheet" href="https://fonts.googleapis.com/css2?family=Roboto:wght@300;400;500;700;900&family=Roboto+Condensed:wght@400;700&display=swap">
<style>
  :root {
    --blue: #2b9fd8;
    --blue-dark: #1d86bd;
    --ink: #333a40;
    --ink-soft: #5d656c;
    --rule: #c9d3da;
    --paper: #ffffff;
    --band-dark: #3a3a3c;
    --stage-top: #9a9a9a;
    --stage-bottom: #6f6f6f;
  }
  * { box-sizing: border-box; margin: 0; padding: 0; }
  html, body { width: 1200px; height: 777px; overflow: hidden; }
  body {
    font-family: "Roboto", Arial, sans-serif;
    color: var(--ink);
    background: radial-gradient(ellipse at 50% 40%, var(--stage-top), var(--stage-bottom));
    position: relative;
  }

  .spread {
    position: absolute; left: 60px; top: 136px;
    width: 1080px; height: 504px; display: flex;
    box-shadow: 0 18px 40px rgba(0,0,0,.35);
    background: var(--paper);
  }
  .panel { width: 360px; height: 504px; position: relative; padding: 18px 14px; overflow: hidden; }
  .panel + .panel { border-left: 1px solid #e6e9ec; }

  /* Panel 1 */
  .p1-title { text-align: center; font-family: "Roboto Condensed", sans-serif; font-weight: 700; color: var(--blue-dark); font-size: 17px; }
  .p1-sub { text-align: center; font-size: 13px; color: var(--ink-soft); font-weight: 300; margin-top: 2px; }
  .cause-band {
    margin: 10px -4px 0; background: var(--blue); color: #fff; text-align: center;
    font-family: "Roboto Condensed", sans-serif; font-weight: 700; font-size: 9px;
    padding: 5px 0; clip-path: polygon(2% 0, 100% 0, 98% 100%, 0 100%);
  }
  .cause-grid { display: grid; grid-template-columns: 66px 1fr 70px; gap: 10px; margin-top: 12px; }
  .trigger-list { text-align: center; }
  .trigger-head { font-family: "Roboto Condensed", sans-serif; font-weight: 700; font-size: 8px; color: var(--blue-dark); margin-bottom: 10px; line-height: 1.2; }
  .trigger { font-size: 6.5px; text-transform: uppercase; color: var(--ink); margin-bottom: 10px; }
  .trigger.accent { color: var(--blue); }
  .trigger-icon { display: block; width: 12px; height: 12px; margin: 4px auto 0; background: var(--ink); border-radius: 3px; }
  .trigger.accent .trigger-icon { background: var(--blue); }
  .trigger-rule { width: 22px; height: 1px; background: var(--rule); margin: 0 auto 8px; }

  .fact-box { border: 1.5px solid var(--blue); text-align: center; padding: 8px 8px; margin-bottom: 10px; }
  .fact-box h3 { font-family: "Roboto Condensed", sans-serif; font-size: 14px; color: var(--blue); font-weight: 700; }
  .fact-box h3 span { font-weight: 400; }
  .fact-box p { font-size: 9px; line-height: 1.35; margin-top: 3px; }
  .fact-box .lead { font-weight: 700; }
  .symptoms { list-style: none; font-size: 9px; line-height: 1.45; margin-top: 6px; }

  /* Panel 2 */
  .p2-title { text-align: center; font-family: "Roboto Condensed", sans-serif; font-size: 16px; color: var(--blue); font-weight: 700; }
  .p2-title span { font-weight: 400; }
  .p2-stat { text-align: center; font-size: 8.5px; font-weight: 700; margin-top: 6px; line-height: 1.3; }
  .p2-stat em { color: var(--blue); font-style: normal; }
  .photo {
    margin: 10px -14px 0; height: 112px;
    background: linear-gradient(110deg, #8fa86c 0%, #c7c39a 45%, #e7d8c5 70%, #a9b48c 100%);
  }
  .p2-question { text-align: center; font-size: 9px; font-weight: 500; margin-top: 14px; }
  .p2-test { text-align: center; font-family: "Roboto Condensed", sans-serif; font-size: 17px; color: var(--blue); font-weight: 700; }
  .p2-test span { font-weight: 400; }
  .short-rule { width: 70px; height: 1px; background: var(--blue); margin: 10px auto; }
  .p2-copy { text-align: center; font-size: 9px; line-height: 1.4; padding: 0 12px; }
  .quote { border-top: 1px solid var(--blue); margin: 22px 10px 0; padding: 10px 0 0 34px; position: relative; }
  .quote::before { content: "\201C"; position: absolute; left: 6px; top: 2px; font-size: 30px; color: var(--blue); font-weight: 700; line-height: 1; }
  .quote p { color: var(--blue); font-size: 9px; line-height: 1.35; }
  .quote cite { display: block; font-style: normal; font-size: 8px; color: var(--ink-soft); margin-top: 4px; }

  /* Panel 3 */
  .p3-title { font-family: "Roboto Condensed", sans-serif; font-size: 16px; color: var(--blue); font-weight: 400; }
  .p3-title b { font-weight: 700; }
  .p3-head { font-size: 8px; font-weight: 700; margin-top: 8px; }
  .p3-copy { font-size: 7px; line-height: 1.4; margin-top: 3px; color: var(--ink-soft); }
  .chart-band {
    margin: 12px -4px 0; background: var(--band-dark); color: #fff; text-align: center;
    font-family: "Roboto Condensed", sans-serif; font-size: 10px; font-weight: 700; padding: 6px 0;
  }
  .chart-band span { color: var(--blue); font-weight: 400; }
  .chart { display: block; margin-top: 6px; font-family: "Roboto", sans-serif; }
</style>
</head>
<body>

<main class="spread">
  <section class="panel">
    <h2 class="p1-title">IS IT ALLERGIES OR NOT?</h2>
    <p class="p1-sub">Knowing makes a difference.</p>
    <div class="cause-band">DIFFERENT CAUSES CAN TRIGGER THE SAME SYMPTOMS</div>
    <div class="cause-grid">
      <div class="trigger-list">
        <div class="trigger-head">ALLERGIC<br>TRIGGERS</div>
        <div class="trigger">Dust mite<span class="trigger-icon" role="img" aria-label="Dust mite icon"></span></div><div class="trigger-rule"></div>
        <div class="trigger accent">Cockroach<span class="trigger-icon" role="img" aria-label="Cockroach icon"></span></div><div class="trigger-rule"></div>
        <div class="trigger">Dog dander<span class="trigger-icon" role="img" aria-label="Dog icon"></span></div><div class="trigger-rule"></div>
        <div class="trigger accent">Cat dander<span class="trigger-icon" role="img" aria-label="Cat icon"></span></div><div class="trigger-rule"></div>
        <div class="trigger">Trees<span class="trigger-icon" role="img" aria-label="Leaf icon"></span></div><div class="trigger-rule"></div>
        <div class="trigger accent">Weeds/Grasses<span class="trigger-icon" role="img" aria-label="Grass icon"></span></div><div class="trigger-rule"></div>
        <div class="trigger">Molds<span class="trigger-icon" role="img" aria-label="Mold spore icon"></span></div>
      </div>
      <div>
        <div class="fact-box"><h3>THE <span>NEED</span></h3><p>Patients want real relief from their symptoms.</p></div>
        <div class="fact-box">
          <h3>THE <span>CHALLENGE</span></h3>
          <p class="lead">Symptoms of allergic and non-allergic causes are similar:</p>
          <ul class="symptoms"><li>Nasal congestion</li><li>Rhinorrhea</li><li>Increased secretions</li><li>Sneezing</li><li>Pruritus</li></ul>
        </div>
        <div class="fact-box"><h3>THE <span>SOLUTION</span></h3><p>Utilize Brevicor IgE testing to discover whether you are allergic.</p></div>
      </div>
      <div class="trigger-list">
        <div class="trigger-head">NON-ALLERGIC<br>TRIGGERS</div>
        <div class="trigger">Cigarette smoke<span class="trigger-icon" role="img" aria-label="Cigarette icon"></span></div><div class="trigger-rule"></div>
        <div class="trigger accent">Air pollution<span class="trigger-icon" role="img" aria-label="Factory icon"></span></div><div class="trigger-rule"></div>
        <div class="trigger">Perfume<span class="trigger-icon" role="img" aria-label="Perfume bottle icon"></span></div><div class="trigger-rule"></div>
        <div class="trigger accent">Temperature change<span class="trigger-icon" role="img" aria-label="Thermometer icon"></span></div><div class="trigger-rule"></div>
        <div class="trigger">Alcohol<span class="trigger-icon" role="img" aria-label="Cocktail glass icon"></span></div><div class="trigger-rule"></div>
        <div class="trigger accent">Infection<span class="trigger-icon" role="img" aria-label="Germ icon"></span></div>
      </div>
    </div>
  </section>

  <section class="panel">
    <h2 class="p2-title">ALLERGIC <span>ASTHMA</span></h2>
    <p class="p2-stat">Approximately <em>60%</em> of adults and <em>90%</em> of children with asthma<br>have allergic triggers.</p>
    <div class="photo" role="img" aria-label="Photo of a woman outdoors using an inhaler"></div>
    <p class="p2-question">Is underlying allergy contributing to your asthma?</p>
    <p class="p2-test">TEST <span>TO KNOW!</span></p>
    <div class="short-rule"></div>
    <p class="p2-copy">Allergic asthma is the most common type of asthma. It is triggered by allergens like dust mites or pet dander.</p>
    <div class="short-rule"></div>
    <p class="p2-copy">Along with a physical exam and review of your medical history, the Brevicor IgE test may help your doctor determine if you have allergic asthma.</p>
    <blockquote class="quote">
      <p>For successful long-term management of asthma, it is essential to identify and reduce exposures to relevant allergens...</p>
      <cite>NRHA Guidelines</cite>
    </blockquote>
  </section>

  <section class="panel">
    <h2 class="p3-title"><b>TAKE CONTROL</b> OF YOUR ALLERGIES</h2>
    <p class="p3-head">Reducing exposure to allergic triggers helps reduce symptoms</p>
    <p class="p3-copy">Now that you know your unique IgE profile, you can take steps to reduce your exposure to these triggers – and help reduce or prevent congestion, sneezing, coughing, wheezing, and other symptoms. Follow the trigger control tips provided on the back of this sheet.</p>
    <p class="p3-head">Allergies add up</p>
    <p class="p3-copy">Although some people may be sensitive to only a single allergen, most people with allergies are sensitive to more than one allergen. For such people, symptoms may appear only when they are exposed to two or more allergic triggers at once. The point when symptoms appear is called the allergic symptom threshold. Reducing exposure to your allergic triggers can help reduce your symptoms. In addition, experts believe that medical treatments are more effective if people also decrease exposure to allergens.</p>
    <div class="chart-band">THE CUMULATIVE EFFECT <span>OF ALLERGENS</span></div>
    <svg class="chart" width="332" height="232" viewBox="0 0 332 232" aria-label="Chart of cumulative allergen effect">
      <line x1="26" y1="10" x2="26" y2="162" stroke="#333a40" stroke-width="1"/>
      <line x1="26" y1="162" x2="330" y2="162" stroke="#333a40" stroke-width="1"/>
      <text x="14" y="150" font-size="6.5" fill="#333a40" transform="rotate(-90 14 150)">CLINICAL MANIFESTATION</text>
      <line x1="26" y1="62" x2="330" y2="62" stroke="#2b9fd8" stroke-width="1" stroke-dasharray="3 2"/>
      <text x="30" y="57" font-size="6.5" fill="#333a40">SYMPTOM THRESHOLD</text>
      <g fill="#2b9fd8">
        <rect x="58" y="72" width="54" height="44"/><rect x="58" y="118" width="54" height="44"/>
        <rect x="142" y="26" width="54" height="44"/><rect x="142" y="72" width="54" height="44"/><rect x="142" y="118" width="54" height="44"/>
        <rect x="236" y="76" width="54" height="28"/><rect x="236" y="105" width="54" height="28"/><rect x="236" y="134" width="54" height="28"/>
      </g>
      <g font-size="6.5" fill="#ffffff" text-anchor="middle">
        <text x="85" y="97">ALLERGEN II</text><text x="85" y="143">ALLERGEN I</text>
        <text x="169" y="51">ALLERGEN III</text><text x="169" y="97">ALLERGEN II</text><text x="169" y="143">ALLERGEN I</text>
        <text x="263" y="93">ALLERGEN III</text><text x="263" y="122">ALLERGEN II</text><text x="263" y="151">ALLERGEN I</text>
      </g>
      <g font-size="6.5" fill="#333a40" text-anchor="middle">
        <text x="85" y="176" font-weight="700" fill="#2b9fd8">SITUATION A</text>
        <text x="85" y="186">Specific IgE is</text><text x="85" y="195">present but there</text><text x="85" y="204">are no symptoms</text>
        <text x="169" y="176" font-weight="700" fill="#2b9fd8">SITUATION B</text>
        <text x="169" y="186">Third allergen exposure</text><text x="169" y="195">creates symptoms when</text><text x="169" y="204">no exposure reduction</text><text x="169" y="213">measures are taken</text>
        <text x="263" y="176" font-weight="700" fill="#2b9fd8">SITUATION C</text>
        <text x="263" y="186">Third allergen exposure does</text><text x="263" y="195">not produce symptoms if</text><text x="263" y="204">exposure reduction measures</text><text x="263" y="213">are taken for allergens I and II</text>
      </g>
    </svg>
  </section>
</main>

</body>
</html>
```